Dental Office Needs- Flyer Design for Same Day Crowns

We need a flyer that will explain the benefits of the same day crown from the patient prospective. Not show pictures of the machine that makes the crowns. See attached material for content. The flyer should use the practices PMS colors of Green 562 and Blue 3025. The ad should say to the patient - I want to go this office and get my crown done there.
Updates

Project Deadline Extended Reason: The difference in the time zone between USA and Europe has caused issues. Minor changes still need to be worked out. Added Thursday, July 14, 2016

Target Market(s)

Dental Patients

Industry/Entity Type

Dental

Requirements
Must have
• Call to Action
• Business Address and Business Logo
• Classic Design
• images of a Happy 50 year old Couple
• Gives the benefits of the same day crown
Should not have
• No Images of tooth figures
• No before or after pictures

```html
<!DOCTYPE html>
<html lang="en">
<head>
<meta charset="utf-8">
<title>Brookfield Dental Care – Same-Day Crowns Flyer</title>
<link href="https://fonts.googleapis.com/css2?family=Arimo:wght@400;700&display=swap" rel="stylesheet">
<style>
  :root {
    --backdrop: #2b2b2b;
    --paper: #ffffff;
    --ink: #1d1d1b;
    --brand-teal: #0f7f7a;
    --brand-blue: #0b4f78;
    --ribbon-red: #e10a17;
    --ribbon-dark: #a8070f;
    --green-light: #2fae68;
    --green-mid: #0c8f4a;
    --green-deep: #0b9a4f;
    --footer-green: #3bb56c;
    --benefit-lime: #95c11f;
    --benefit-red: #e30613;
    --benefit-purple: #662483;
    --benefit-pink: #d60b52;
    --photo-top: #e6e0d6;
    --photo-bottom: #cfc2ae;
  }
  * { margin: 0; padding: 0; box-sizing: border-box; }
  html, body { width: 1200px; height: 1200px; overflow: hidden; background: var(--backdrop); }
  body { position: relative; font-family: "Arimo", Arial, sans-serif; color: var(--ink); }

  .flyer {
    position: absolute; left: 146px; top: 12px;
    width: 1056px; height: 1366px;
    background: var(--paper);
    transform: scale(0.8638); transform-origin: top left;
  }
  .logo-card {
    position: absolute; left: 33px; top: 28px; width: 380px; height: 182px;
    background: var(--paper); box-shadow: 0 3px 8px rgba(0,0,0,.35);
    display: flex; align-items: center; justify-content: center; gap: 12px;
  }
  .logo-card .logo-dot { width: 22px; height: 22px; border-radius: 50%; background: var(--brand-teal); }
  .logo-card .logo-name { font-size: 30px; font-weight: 400; color: var(--brand-teal); }

  .ribbon { position: absolute; left: 66px; top: 242px; width: 400px; height: 372px; }
  .ribbon-text {
    position: absolute; left: 110px; top: 335px; width: 330px;
    text-align: center; color: #fff; font-weight: 700; font-size: 48px; line-height: 58px;
  }

  .photo {
    position: absolute; left: 446px; top: 28px; width: 578px; height: 640px;
    background: linear-gradient(160deg, var(--photo-top), var(--photo-bottom));
  }

  .intro { position: absolute; left: 53px; top: 630px; width: 362px; font-size: 16.5px; line-height: 21px; text-align: justify; }
  .ask { position: absolute; left: 53px; top: 733px; width: 362px; font-size: 18.5px; line-height: 24px; }
  .claim {
    position: absolute; left: 40px; top: 802px; width: 370px;
    text-align: center; color: var(--brand-blue); font-size: 20px; line-height: 25px; text-transform: uppercase;
  }

  .benefits { position: absolute; left: 123px; top: 932px; width: 225px; }
  .benefit {
    height: 68px; border-radius: 4px; color: #fff; font-size: 19px; line-height: 25px;
    display: flex; align-items: center; justify-content: center; text-align: center;
  }
  .benefit.lime { background: var(--benefit-lime); }
  .benefit.red { background: var(--benefit-red); }
  .benefit.purple { background: var(--benefit-purple); }
  .benefit.pink { background: var(--benefit-pink); }
  .plus { height: 21px; position: relative; }
  .plus::before, .plus::after { content: ""; position: absolute; background: var(--benefit-red); }
  .plus::before { left: 100px; top: 9px; width: 30px; height: 6px; }
  .plus::after { left: 112px; top: -4px; width: 6px; height: 32px; }

  .goodbye {
    position: absolute; left: 446px; width: 577px; color: #fff;
    border-radius: 16px; padding: 8px 0 0 30px; font-size: 72px; line-height: 86px;
    border: 2px solid rgba(255,255,255,.85);
  }
  .goodbye.crown { top: 656px; height: 270px; background: var(--green-light); z-index: 3; }
  .goodbye.visit { top: 922px; height: 206px; background: var(--green-mid); z-index: 2; }
  .goodbye.tray { top: 1124px; height: 168px; background: var(--green-deep); font-weight: 400; letter-spacing: -2px; z-index: 1; padding-top: 2px; }
  .goodbye.crown, .goodbye.visit { font-weight: 400; -webkit-text-stroke: 1px #fff; }

  .footer {
    position: absolute; left: 0; bottom: 0; width: 100%; height: 56px;
    background: var(--footer-green); color: #fff; font-size: 20px; font-weight: 700;
    display: flex; align-items: center; justify-content: center; gap: 14px;
  }
</style>
</head>
<body>
  <main class="flyer">
    <div class="logo-card">
      <span class="logo-dot"></span>
      <span class="logo-name">Brookfield Dental Care</span>
    </div>

    <svg class="ribbon" viewBox="0 0 400 372" aria-hidden="true">
      <polygon points="4,40 300,0 290,28 4,135" fill="var(--ribbon-dark)"/>
      <polygon points="4,40 290,28 250,372 4,135" fill="var(--ribbon-red)"/>
      <polygon points="30,85 392,108 370,300 180,310 60,280" fill="var(--ribbon-red)"/>
      <polygon points="180,290 290,300 280,320 190,360" fill="var(--ribbon-dark)"/>
    </svg>
    <div class="ribbon-text">2 HOURS<br>INSTEAD OF<br>2 VISITS.</div>

    <div class="photo" role="img" aria-label="Photo of a smiling couple in their fifties in a home kitchen, the man slicing vegetables"></div>

    <p class="intro">Introducing crowns, veneers and bridges that happen in hours instead of days – no more temporaries, no more multiple visits, no messy dental impressions.</p>
    <p class="ask">Ask your dentist if a same-day restoration is right for you.</p>
    <p class="claim">When it comes to your next crown or veneer, the benefits of a digital restoration add up quickly.</p>

    <div class="benefits">
      <div class="benefit lime">A same-day<br>Restoration</div>
      <div class="plus"></div>
      <div class="benefit red">A stronger,<br>more precise fit</div>
      <div class="plus"></div>
      <div class="benefit purple">A beautiful,<br>natural appearance</div>
      <div class="plus"></div>
      <div class="benefit pink">A relaxing<br>Patient experience</div>
    </div>

    <div class="goodbye crown">GOOD BYE<br>TEMPORARY<br>CROWN</div>
    <div class="goodbye visit">GOOD BYE<br>SECOND VISIT.</div>
    <div class="goodbye tray">GOOD BYE<br>GOOEY TRAY</div>

    <footer class="footer">
      <span>418 Maple Ridge Rd. Oakdale, MI 48000</span><span>I</span>
      <span>555.014.2280</span><span>I</span>
      <span>info@brookfielddentalcare.com</span>
    </footer>
  </main>
</body>
</html>
```